Residential & commercial cleaning business

Looking for Brazilian colors, green/blue/yellow.
Name of business is “Marta’s Cleaning”.
Second side of card will be for ‘confirming customer next appointment date/time.
Want to include in description…residential & commercial cleaning, experienced, highly recommended, reasonable rates, free estimates, Marta’sCleaningNH@brightmail.example, Brookhaven Ridge, NH, Call today at 603.555.0148.

```html
<!DOCTYPE html>
<html lang="en">
<head>
<meta charset="utf-8">
<title>Marta’s Cleaning – Business Card</title>
<link rel="stylesheet" href="https://fonts.googleapis.com/css2?family=Montserrat:wght@400;500;700&family=Allura&display=swap">
<style>
  :root {
    --backdrop: #676767;
    --brand-blue: #0f76f5;
    --brand-teal: #10dccb;
    --paper: #ffffff;
  }
  html, body {
    margin: 0;
    width: 1200px;
    height: 1200px;
    overflow: hidden;
    background: var(--backdrop);
  }
  .canvas {
    position: relative;
    width: 1200px;
    height: 1200px;
  }
  .card {
    position: absolute;
    left: 174px;
    width: 851px;
    height: 472px;
    display: block;
    box-shadow: 0 14px 22px -12px rgba(0,0,0,0.45);
  }
  .card--front { top: 102px; }
  .card--back { top: 625px; }
  .sans { font-family: "Montserrat", sans-serif; }
  .script { font-family: "Allura", cursive; }
  .fill-blue { fill: var(--brand-blue); }
  .fill-teal { fill: var(--brand-teal); }
  .fill-white { fill: var(--paper); }
</style>
</head>
<body>
<main class="canvas">

  <!-- Front side -->
  <svg class="card card--front" viewBox="0 0 1063 590" aria-label="Front of business card">
    <rect class="fill-blue" width="1063" height="590"/>
    <path class="fill-teal" d="M0,407 C140,325 290,318 425,350 C555,382 640,432 715,447 L950,447 C1050,320 1065,130 975,0 L0,0 Z"/>
    <path class="fill-white" d="M0,380 C140,300 290,295 430,325 C560,355 650,415 695,430 L930,430 C1030,320 1040,130 952,0 L0,0 Z"/>

    <g class="brand-name">
      <circle class="fill-teal" cx="418" cy="110" r="16"/>
      <text class="sans fill-blue" x="270" y="200" font-size="54" font-weight="700" text-anchor="middle">Marta’s Cleaning</text>
    </g>

    <g class="services sans fill-blue" font-size="45" font-weight="500">
      <text x="576" y="142">Residential</text>
      <text x="576" y="187">&amp; Commercial</text>
      <text x="576" y="232">Cleaning</text>
    </g>
    <rect class="fill-teal" x="582" y="255" width="313" height="2"/>

    <g class="benefits sans fill-blue" font-size="18.5" font-weight="500">
      <text x="613" y="290">EXPERIENCED</text>
      <text x="613" y="316">HIGHLY RECOMMENDED</text>
      <text x="613" y="342">REASONABLE RATES</text>
      <text x="613" y="368">FREE ESTIMATES</text>
    </g>
    <g class="ticks" fill="none" stroke="var(--brand-teal)" stroke-width="3.5" stroke-linecap="round" stroke-linejoin="round">
      <path d="M589,283 l5,7 l10,-17"/>
      <path d="M589,309 l5,7 l10,-17"/>
      <path d="M589,335 l5,7 l10,-17"/>
      <path d="M589,361 l5,7 l10,-17"/>
    </g>

    <text class="sans fill-blue" x="740" y="430" font-size="21" font-weight="700">Text today at.</text>
    <rect class="fill-teal" x="662" y="446" width="318" height="84" rx="42"/>
    <text class="sans fill-white" x="828" y="501" font-size="35" font-weight="700" text-anchor="middle">603.555.0148</text>

    <g class="contact sans fill-white" font-weight="500">
      <text x="113" y="460" font-size="29">Brookhaven Ridge, NH</text>
      <text x="113" y="506" font-size="26">Marta’sCleaningNH@brightmail.example</text>
    </g>
  </svg>

  <!-- Back side -->
  <svg class="card card--back" viewBox="0 0 1063 590" aria-label="Back of business card, appointment reminder">
    <rect class="fill-blue" width="1063" height="590"/>
    <path class="fill-teal" d="M86,590 C15,510 -5,370 50,280 C110,180 230,175 330,210 C430,245 490,300 560,300 C760,300 930,310 1063,255 L1063,590 Z"/>
    <path class="fill-white" d="M112,590 C45,510 30,380 75,300 C125,210 230,205 325,238 C425,273 490,323 560,323 C760,323 935,330 1063,280 L1063,590 Z"/>

    <text class="script fill-white" x="107" y="160" font-size="104" textLength="875" lengthAdjust="spacingAndGlyphs">Your next Appointment</text>

    <g class="appointment-fields">
      <rect class="fill-teal" x="87" y="197" width="415" height="82" rx="41"/>
      <rect class="fill-teal" x="554" y="197" width="416" height="82" rx="41"/>
      <rect class="fill-teal" x="87" y="298" width="883" height="82" rx="41"/>
      <g class="sans fill-white" font-size="29" font-weight="500">
        <text x="120" y="248">Date:</text>
        <text x="594" y="248">Time:</text>
        <text x="120" y="350">Details:</text>
      </g>
    </g>

    <g class="contact sans fill-blue" text-anchor="middle" font-weight="500">
      <text x="532" y="427" font-size="29">Brookhaven Ridge, NH</text>
      <text x="532" y="474" font-size="27">Marta’sCleaningNH@brightmail.example</text>
    </g>
    <text class="script fill-blue" x="532" y="526" font-size="46" text-anchor="middle">Your referrals are appreciated</text>
  </svg>

</main>
</body>
</html>
```